Contractor Business Card Design

Looking to have a card made that has a bold description of (KITCHENS, BASEMENTS, BATHROOMS)

Definition and layers a plus

Contact info is;

Mark T. Ellery
Larkfield, MN 55099
Cell: 612-555-0147
website: www.cobaltfinishworks.example
Email: cobaltfinishworksmn@mailbox.example

colors: red, black, gray, white

Contact Information for Business Card

Contact info is;

Mark T. Ellery
Larkfield, MN 55099
Cell: 612-555-0147

Colors
ec1f27

Requirements
Must have
• Looking for layers and definition
Nice to have
• Cards are planned to be printed on plastic cards

```html
<!DOCTYPE html>
<html lang="en">
<head>
<meta charset="utf-8">
<title>Cobalt Finishworks – Business Card</title>
<link href="https://fonts.googleapis.com/css2?family=Ubuntu:wght@400;500;700&display=swap" rel="stylesheet">
<style>
  :root{
    --red:#dc2727;
    --ink:#232323;
    --black:#0b0b0b;
    --white:#ffffff;
    --backdrop:#9b9b9b;
    --text:#2e2e2e;
  }
  html,body{margin:0;padding:0;overflow:hidden}
  body{width:1021px;height:1200px;background:var(--backdrop);position:relative;font-family:'Ubuntu',sans-serif}
  .card{position:absolute;width:753px;height:429px;overflow:hidden}
  .card-front{left:134px;top:119px;background:var(--ink)}
  .card-back{left:131px;top:650px;background:var(--white)}

  .brand-ring{position:absolute;border-radius:50%;box-sizing:border-box}
  .card-front .brand-ring{left:303px;top:74px;width:144px;height:144px;border:5px solid var(--red)}
  .card-back .brand-ring{left:83px;top:40px;width:112px;height:112px;border:4px solid var(--red)}

  .brand-name{position:absolute;font-weight:700;text-align:center;text-transform:uppercase;line-height:1}
  .card-front .brand-name{left:0;width:753px;top:234px;color:var(--white);font-size:50px;letter-spacing:3px;padding-left:3px;box-sizing:border-box}
  .card-front .brand-name span{display:block;color:var(--red);font-size:20px;letter-spacing:9px;padding-left:9px;margin-top:14px}
  .card-back .brand-name{left:40px;width:200px;top:165px;color:var(--black);font-size:40px;letter-spacing:1px}
  .card-back .brand-name span{display:block;color:var(--red);font-size:15px;letter-spacing:7px;padding-left:7px;margin-top:11px}

  .service-band{position:absolute;left:0;top:348px;width:753px;height:49px}
  .service-band svg{position:absolute;left:0;top:0}
  .service-list{position:absolute;left:194px;top:0;height:49px;display:flex;align-items:center;gap:14px;margin:0;padding:0;list-style:none;color:var(--white);font-size:18px;font-weight:400;letter-spacing:.3px}
  .service-list li::before{content:"";display:inline-block;width:7px;height:7px;border-radius:50%;background:var(--ink);margin-right:9px;vertical-align:middle;position:relative;top:-2px}

  .card-back .arcs{position:absolute;left:0;top:0}
  .contact{position:absolute;left:425px;top:212px;color:var(--text)}
  .contact-name{margin:0;color:var(--red);font-size:31px;font-weight:500;line-height:1}
  .contact-role{margin:6px 0 0;font-size:17px;line-height:1}
  .contact-list{list-style:none;margin:20px 0 0;padding:0;font-size:17px}
  .contact-list li{display:flex;align-items:center;height:24.6px}
  .contact-list svg{width:14px;height:14px;margin-right:8px;flex:none}
</style>
</head>
<body>

<section class="card card-front">
  <div class="brand-ring"></div>
  <div class="brand-name">Cobalt<span>Finishworks</span></div>

  <div class="service-band">
    <svg width="753" height="49" viewBox="0 0 753 49">
      <polygon points="0,0 115,0 133,24.5 115,49 0,49" fill="var(--white)"/>
      <polygon points="115,0 127,0 145,24.5 127,49 115,49 133,24.5" fill="var(--black)"/>
      <polygon points="127,0 753,0 753,49 127,49 145,24.5" fill="var(--red)"/>
    </svg>
    <ul class="service-list">
      <li>KITCHENS</li>
      <li>BASEMENTS</li>
      <li>BATHROOMS</li>
    </ul>
  </div>
</section>

<section class="card card-back">
  <svg class="arcs" width="753" height="429" viewBox="0 0 753 429">
    <path fill="var(--black)" d="M384,156 A268,268 0 0 1 753,166 L753,207 A224,224 0 0 0 384,160 Z"/>
    <path fill="var(--red)" d="M333,429 A237,237 0 0 1 707,159 L695,160 A220,220 0 0 0 362,429 Z"/>
  </svg>

  <div class="brand-ring"></div>
  <div class="brand-name">Cobalt<span>Finishworks</span></div>

  <div class="contact">
    <h1 class="contact-name">Mark T. Ellery</h1>
    <p class="contact-role">Co-Founder</p>
    <ul class="contact-list">
      <li><svg viewBox="0 0 24 24"><path fill="var(--red)" d="M6.6 10.8a15.1 15.1 0 0 0 6.6 6.6l2.2-2.2a1 1 0 0 1 1-.25 11.4 11.4 0 0 0 3.6.57 1 1 0 0 1 1 1V20a1 1 0 0 1-1 1A17 17 0 0 1 3 4a1 1 0 0 1 1-1h3.5a1 1 0 0 1 1 1c0 1.25.2 2.45.57 3.570a1 1 0 0 1-.25 1z"/></svg>612-555-0147</li>
      <li><svg viewBox="0 0 24 24"><path fill="var(--red)" d="M2 5h20v14H2z"/><path fill="none" stroke="var(--white)" stroke-width="1.6" d="M2 5l10 8 10-8M2 19l8-7M22 19l-8-7"/></svg>cobaltfinishworksmn@mailbox.example</li>
      <li><svg viewBox="0 0 24 24"><circle cx="12" cy="12" r="10" fill="var(--red)"/><path fill="none" stroke="var(--white)" stroke-width="1.4" d="M2 12h20M12 2c3 3 3 17 0 20M12 2c-3 3-3 17 0 20"/></svg>www.cobaltfinishworks.example</li>
      <li><svg viewBox="0 0 24 24"><path fill="var(--red)" d="M12 1a8 8 0 0 0-8 8c0 6 8 14 8 14s8-8 8-14a8 8 0 0 0-8-8zm0 11a3 3 0 1 1 0-6 3 3 0 0 1 0 6z"/></svg>Larkfield, MN 55099</li>
    </ul>
  </div>
</section>

</body>
</html>
```